Web Design Project for a Software & Consulting Company

We have just completed a recent ArtFlock project for a new logo (see attached).
As the next stage of our rebranding we now require a website re-design to complement the new logo.
Our current site, http://www.rigsumsoft.example was built in-house and does not come across as professional as we would like. We supply software and associated services to some of the world’s largest oil companies and we need our site to reflect that level of client.
We will also be posting another design project for brochures, PowerPoint slides and other materials very soon.
We would like designs for…
Home page
Product page
• QTV
• BLZ
• FNQ
Services
News page
About Us page
Contact Us page
Page for mobile devices that gives basic company and product information
Currently the site is small but we intend to increase content to include white papers etc. this should be taken into account when designing the navigation therefore we would prefer navigation through styled text links rather than images.
Colour schemes should broadly be taken from our new logo, where the dark blue and dark green from the left and right sides of the logo are the main colours, but other, brighter accent colours can be used to highlight sections or content.
Dark Blue = C:88, M:55, Y:44, K:28
Dark Green = C:87, M:53, Y:50, K:50
NB: Don’t use the logo on our current site, make sure you use the one attached.
We would prefer the final file format to be a layered PSD.
The site should be clean and professional and communicate the following...
• That we have a great depth and breadth of knowledge about our customers’ business, enabling us to deliver the best systems and solutions.
• That we are a leading provider of cost estimation and control solutions to the oil and gas industry.
• The benefits of our software and consulting services.
• Show that we deliver outstanding customer service and value with a very high level of professionalism
• The site should have no Flash and be able to self-adjust to fit any screen size.
Things to avoid …
• Obvious and clichéd oil industry imagery, no oil rigs
• Cartoon style graphics
Our Background
We are an integrated software and consulting organization specialising in the drilling side of the oil and gas industry. Simply put our software helps companies better understand, predict and communicate the cost of drilling wells.
We have 3 software products and a consulting offering consisting of…
• QTV - Probabilistic time and cost software
• BLZ – Cost tracking and reporting software
• FNQ – (currently known as BoreMemory) – Lessons learned software
• Consulting services
Our systems are in use in over 30 countries with a broad range of clients including: GN, Solvane, Prue, Tolmar, VONI Kelstra, SALVEM and Quorlit.
Our current site can be found at www.rigsumsoft.example
Our main competitors are
• http://www.gavondel.example/
• http://www.mirrowen.example/
• http://www.tbx.example/services/software-solutions/p1-
Our depth of drilling knowledge, quality of software and collaboration with clients differentiate us form the competition.
We strive for very high levels of customer service.
We look forward to receiving your designs!
Updates
Thanks to all the designers who have submitted a design, we appreciate the effort.
We will do our best to give individual feedback on each design but given that many are quite similar we thought we would give some general feedback first.
Nearly all the designs submitted so far have been slight variations on…
-
Top Menu
-
Scrolling Photo Banner
-
4 Columns
-
Body
-
Deep Footer
These designs are well executed but they are basically the same layout as our existing site and while there is nothing inherently wrong with this layout we would like to see some designs that are a bit more innovative and different. We don’t really want just a polished version of our current site.
Thanks again,
RST
Thanks to everyone who has submitted a design, the response has been great.
We are close to making a decision so if you are intending to submit a design please do it soon, the deadline is only a few days away.
Thanks again.
RST
Target Market(s)
Mid to high level executives
Industry/Entity Type
Oil And Gas
Look and feel

```html
<!DOCTYPE html>
<html lang="en">
<head>
<meta charset="utf-8">
<title>Rigsum Soft — Home</title>
<link href="https://fonts.googleapis.com/css2?family=Questrial&family=Montserrat:wght@400;600;700&family=Arimo:wght@400&display=swap" rel="stylesheet">
<style>
:root{
  --teal:#466d7a;
  --teal-dark:#1f4b57;
  --olive:#9cab6f;
  --olive-dark:#7f9150;
  --ink:#2b2b2b;
  --muted:#555;
  --grey:#a9a9a9;
  --sky-top:#d3ebf6;
  --sky-mid:#eef6fa;
  --footer:#e3e3e3;
}
*{box-sizing:border-box;margin:0;padding:0}
html,body{width:1057px;height:1200px;overflow:hidden;background:#fff}
body{position:relative;font-family:"Arimo",Arial,sans-serif;color:var(--ink)}
.hero-bg{position:absolute;left:0;top:0;width:1057px;height:445px;
  background:linear-gradient(180deg,var(--sky-top) 0%,var(--sky-mid) 45%,#dde9ee 72%,#fff 100%)}
.brand{position:absolute;display:flex;align-items:center;gap:8px;font-family:"Montserrat",sans-serif;font-weight:700;color:var(--teal-dark);letter-spacing:.5px;white-space:nowrap}
.brand-dot{border-radius:50%;background:var(--teal);flex:none}
.brand--header{left:142px;top:26px;font-size:22px}
.brand--header .brand-dot{width:34px;height:34px}
.main-nav{position:absolute;left:452px;top:30px;width:446px;height:40px;border:2px solid #e7eef1;background:rgba(255,255,255,.75);border-radius:3px;display:flex;align-items:center;padding-left:16px}
.main-nav a{font-family:"Questrial",sans-serif;font-size:10.5px;color:#1d1d1d;text-decoration:none;margin-right:19px;letter-spacing:.1px;white-space:nowrap}
.main-nav a:last-child{margin-right:0}
.main-nav .current{display:flex;align-items:center;gap:7px;margin-right:11px}
.main-nav .current::before{content:"";width:40px;height:3px;background:var(--olive)}
.hero-media{position:absolute;left:198px;top:138px;width:306px;height:276px;border-radius:6px;
  background:linear-gradient(180deg,#2c2c2c 0%,#3a3a3a 66%,#cfd3d6 67%,#eef0f1 100%)}
.hero-title{position:absolute;left:496px;top:174px;width:400px;text-align:center;font-family:"Questrial",sans-serif;color:var(--teal-dark);font-size:24px;line-height:26px;letter-spacing:.5px}
.hero-title b{color:var(--olive-dark);font-family:"Montserrat",sans-serif;font-weight:700}
.hero-title .big{display:block;font-family:"Montserrat",sans-serif;font-weight:700;font-size:36px;line-height:42px;color:var(--teal)}
.slide-arrow{position:absolute;top:233px;width:24px;height:24px}
.slide-arrow--prev{left:29px}.slide-arrow--next{left:996px}
.thumb-line{position:absolute;left:600px;top:381px;width:380px;height:1px;background:linear-gradient(90deg,transparent,#a9b88a 30%,#a9b88a 70%,transparent)}
.thumb{position:absolute;top:354px;width:54px;height:54px;border-radius:50%;border:3px solid #fff;box-shadow:0 1px 3px rgba(0,0,0,.3)}
.thumb--screen{left:707px;background:var(--teal-dark)}
.thumb--team{left:765px;background:linear-gradient(135deg,#c9c9c0,#6f6a5c)}
.thumb--support{left:823px;background:linear-gradient(135deg,#f0f0f0,#a8a8a8)}
.tiles{position:absolute;left:124px;top:451px;width:803px;height:457px;display:grid;grid-template-columns:repeat(4,1fr);grid-template-rows:228px 229px}
.tile{position:relative;padding:20px 20px 0 20px;overflow:hidden}
.tile--teal{background:var(--teal);color:#fff}
.tile--olive{background:var(--olive);color:#fff}
.tile--white{background:#fff}
.tile-kicker{display:flex;align-items:center;gap:6px;font-family:"Montserrat",sans-serif;font-weight:600;font-size:10px;letter-spacing:.5px}
.tile-kicker::after{content:"";width:20px;height:1px;background:currentColor}
.tile--teal .tile-kicker{color:#b9c58e}
.tile--white .tile-kicker{color:var(--olive-dark)}
.tile-title{font-family:"Montserrat",sans-serif;font-weight:600;font-size:15px;line-height:19px;letter-spacing:.5px;margin-top:12px;text-transform:uppercase}
.tile--white .tile-title{color:var(--teal-dark)}
.tile p{position:relative;z-index:1;font-size:10px;line-height:12.5px;margin-top:6px}
.tile--white p{color:var(--muted)}
.tile-art{position:absolute}
.tile-list{list-style:none;margin-top:18px}
.tile-list li{font-size:10px;line-height:12px;color:#33412a;margin-bottom:14px;padding-left:18px;position:relative}
.tile-list--dash li::before{content:"";position:absolute;left:0;top:6px;width:8px;height:1px;background:#33412a}
.tile-list--doc li::before{content:"";position:absolute;left:0;top:0;width:11px;height:13px;background:#c0312b}
.contact{display:flex;gap:8px;font-size:10px;line-height:13px;color:var(--muted);margin-top:18px}
.contact svg{flex:none}
.clients-title{position:absolute;left:124px;top:962px;width:810px;text-align:center;font-family:"Montserrat",sans-serif;font-weight:700;font-size:36px;color:var(--teal-dark);letter-spacing:.5px}
.clients-title::before,.clients-title::after{content:"";position:absolute;top:22px;width:268px;height:2px;background:#dde3dc}
.clients-title::before{left:0}.clients-title::after{right:0}
.client-list{position:absolute;left:160px;top:1036px;width:740px;display:flex;justify-content:space-between;align-items:center}
.client{display:flex;align-items:center;gap:6px;font-family:"Montserrat",sans-serif;font-weight:600;font-size:22px;color:var(--grey)}
.client--accent{color:#4aa336}
.client-mark{width:14px;height:14px;background:currentColor}
.site-footer{position:absolute;left:0;top:1133px;width:1057px;height:67px;background:var(--footer);border-bottom:4px solid var(--teal-dark)}
.brand--footer{left:140px;top:22px;font-size:12px;gap:6px;color:#8a8a8a}
.brand--footer .brand-dot{width:22px;height:22px;background:#a5a5a5}
.copyright{position:absolute;left:278px;top:30px;font-size:9.5px;color:#333;white-space:nowrap}
.share{position:absolute;left:742px;top:26px;display:flex;align-items:center;gap:4px;font-family:"Montserrat",sans-serif;font-weight:600;font-size:9px;color:#222}
.share span.dot{width:14px;height:14px;border-radius:50%;background:#8d8d8d}
.share span.label{margin-right:4px}
</style>
</head>
<body>
<div class="hero-bg"></div>

<header>
  <div class="brand brand--header"><span class="brand-dot"></span>RIGSUM SOFT</div>
  <nav class="main-nav">
    <a class="current" href="#">HOME</a>
    <a href="#">ABOUT US</a>
    <a href="#">PRODUCT</a>
    <a href="#">SERVICES</a>
    <a href="#">NEWS</a>
    <a href="#">CONTACT US</a>
  </nav>
</header>

<section class="hero">
  <div class="hero-media" role="img" aria-label="Desktop monitor showing QTV probabilistic time and cost software with a line chart"></div>
  <h1 class="hero-title">RST HAVE THE <b>TOOLS</b> TO HELP<br>COMPANIES <b>BETTER MANAGE</b><br>THE BUSINESS OF<span class="big">DRILLING WELLS</span></h1>
  <svg class="slide-arrow slide-arrow--prev" viewBox="0 0 24 24"><circle cx="12" cy="12" r="12" fill="#6d8a34"/><path d="M14 7l-5 5 5 5" stroke="#fff" stroke-width="2.4" fill="none"/></svg>
  <svg class="slide-arrow slide-arrow--next" viewBox="0 0 24 24"><circle cx="12" cy="12" r="12" fill="#6d8a34"/><path d="M10 7l5 5-5 5" stroke="#fff" stroke-width="2.4" fill="none"/></svg>
  <div class="thumb-line"></div>
  <div class="thumb thumb--screen" role="img" aria-label="Software on a monitor"></div>
  <div class="thumb thumb--team" role="img" aria-label="Business team meeting"></div>
  <div class="thumb thumb--support" role="img" aria-label="Customer support agent with headset"></div>
</section>

<section class="tiles">
  <article class="tile tile--teal">
    <div class="tile-kicker">PLAN</div>
    <h2 class="tile-title">Time &amp;<br>Cost Estimation</h2>
    <p>QTV delivers a standardized, systematic approach to understanding, quantifying and communicating...</p>
    <div class="tile-art" role="img" aria-label="Two business people reviewing documents" style="left:0;top:144px;width:128px;height:84px;background:linear-gradient(180deg,#8aa0a6,#2f3a3f)"></div>
  </article>
  <article class="tile tile--white">
    <div class="tile-kicker">EXECUTE</div>
    <h2 class="tile-title">Materials &amp;<br>Cost Control</h2>
    <p style="width:122px">Since 1992 BLZ has been helping companies optimize their materials and logistics processes and accurately track costs on a daily basis.</p>
    <div class="tile-art" role="img" aria-label="Businesswoman working at a laptop" style="left:150px;top:100px;width:51px;height:128px;background:linear-gradient(180deg,#e6e6e6,#5b5b5b)"></div>
  </article>
  <article class="tile tile--teal">
    <div class="tile-kicker">LEARN</div>
    <h2 class="tile-title">Lessons<br>Learned</h2>
    <p style="width:112px">BoreMemory is an advanced lessons learned and knowledge management system for use in the Oil &amp; Gas industry...</p>
    <div class="tile-art" role="img" aria-label="Stacked letter blocks" style="left:148px;top:68px;width:38px;height:108px;background:linear-gradient(180deg,#b9c1c4,#4a5357)"></div>
  </article>
  <article class="tile tile--white">
    <div class="tile-kicker">EMBED</div>
    <h2 class="tile-title">Services &amp;<br>Consulting</h2>
    <p style="width:120px">Software solutions rely on people and processes to deliver results...</p>
    <div class="tile-art" role="img" aria-label="Consultant wearing a headset" style="left:118px;top:138px;width:83px;height:90px;background:linear-gradient(180deg,#d6d6d6,#2d2d2d)"></div>
  </article>

  <article class="tile tile--white" style="padding-left:8px">
    <h2 class="tile-title" style="margin-top:2px;font-size:11.5px;display:flex;align-items:center;gap:6px">A Bit About Us <svg width="22" height="6"><path d="M0 3h20M17 0l3 3-3 3" stroke="#1f4b57" fill="none"/></svg></h2>
    <div class="tile-art" role="img" aria-label="Ring of metal spheres" style="left:26px;top:44px;width:92px;height:92px;border-radius:50%;background:radial-gradient(circle,#fff 30%,#9a9a9a 55%,#e4e4e4 75%,#fff 80%)"></div>
    <p style="position:absolute;left:8px;top:152px;width:185px">Rigsum Soft have developed and continue to support software in over 30 countries, providing real results to hundreds of drilling operations.</p>
  </article>
  <article class="tile tile--olive">
    <div class="tile-kicker" style="color:#2d3d1f">NEWS</div>
    <h2 class="tile-title" style="margin-top:4px">Our Updates</h2>
    <ul class="tile-list tile-list--dash">
      <li>QTV Selected by Velmor Gasnet</li>
      <li>BLZ Implementation at Stranvik</li>
      <li>QTV 4.1 Installation for Solvane Canada</li>
    </ul>
    <div class="tile-art" role="img" aria-label="Megaphone" style="left:142px;top:160px;width:56px;height:66px;background:linear-gradient(135deg,#2f8fa0,#1a4f5c)"></div>
  </article>
  <article class="tile tile--white">
    <div class="tile-kicker" style="font-size:9.5px">FIND US &amp;</div>
    <h2 class="tile-title" style="margin-top:4px">Get Connected</h2>
    <div class="contact"><svg width="28" height="28" viewBox="0 0 28 28"><circle cx="14" cy="14" r="13" fill="#dfe6cf" stroke="#9cab6f"/><path d="M14 7a5 5 0 0 1 5 5c0 4-5 9-5 9s-5-5-5-9a5 5 0 0 1 5-5z" fill="#466d7a"/><circle cx="14" cy="12" r="1.8" fill="#fff"/></svg><div>18 Corran Row<br>Dunmore, DN4 2QT</div></div>
    <div class="contact"><svg width="28" height="28" viewBox="0 0 28 28"><circle cx="14" cy="14" r="13" fill="#dfe6cf" stroke="#9cab6f"/><path d="M14 7a5 5 0 0 1 5 5c0 4-5 9-5 9s-5-5-5-9a5 5 0 0 1 5-5z" fill="#466d7a"/><circle cx="14" cy="12" r="1.8" fill="#fff"/></svg><div>4100 Harlow Park Way,<br>Suite 210<br>Calder, TX 70418</div></div>
  </article>
  <article class="tile tile--olive">
    <div class="tile-kicker" style="color:#2d3d1f;font-size:9.5px">DOWNLOAD</div>
    <h2 class="tile-title" style="margin-top:4px">Whitepapers</h2>
    <ul class="tile-list tile-list--doc">
      <li>QTV Selected by Velmor Gasnet</li>
      <li>BLZ Implementation at Stranvik</li>
      <li>QTV 4.1 Installation for Solvane Canada</li>
    </ul>
    <div class="tile-art" role="img" aria-label="Bundle of papers tied with string" style="left:120px;top:176px;width:76px;height:50px;background:linear-gradient(180deg,#f2f2f2,#9b9b9b)"></div>
  </article>
</section>

<section class="clients">
  <h2 class="clients-title">OUR CLIENTS</h2>
  <div class="client-list">
    <span class="client"><span class="client-mark"></span>Prue</span>
    <span class="client">Tolmar</span>
    <span class="client client--accent">GN</span>
    <span class="client">Meridane</span>
    <span class="client">Korrawin</span>
    <span class="client"><span class="client-mark"></span>VONI</span>
  </div>
</section>

<footer class="site-footer">
  <div class="brand brand--footer"><span class="brand-dot"></span>RIGSUM SOFT</div>
  <div class="copyright">© &nbsp;Copy Rights. All Rights Reserved</div>
  <div class="share"><span class="label">SHARE THE WORD RIGSUM SOFT</span><span class="dot"></span><span class="dot"></span></div>
</footer>
</body>
</html>
```